Torvel, Inc. new buisness cards - brand guide included

We need new business cards. SLEAK SIMPLE FINANCE. They must include a place for NAME, TITLE, CELL, OFFICE PHONE, EMAIL. they also must include our services across the bottom. AIR, OCEAN, FTL, LTL, EXPRESS. for reference this will be being handed to some of the most prestigious shipping companies in a america.

Target Market(s)

Finance and corporate

Contact Information for Business Card

We need new business cards. SLEAK SIMPLE FINANCE. They must include a place for NAME, TITLE, CELL, OFFICE PHONE, EMAIL. they also must include our services across the bottom. AIR, OCEAN, FTL, LTL, EXPRESS.

Requirements
Must have
• We need new business cards. SLEAK SIMPLE FINANCE. They must include a place for NAME, TITLE, CELL, OFFICE PHONE, EMAIL. they also must include our services across the bottom. AIR, OCEAN, FTL, LTL, EXPRESS.
Nice to have
• USE THE COLORS AND LOGO IN THE BRAND GUIDE :)

```html
<!DOCTYPE html>
<html lang="en">
<head>
<meta charset="utf-8">
<title>Torvel, Inc. Business Cards</title>
<link href="https://fonts.googleapis.com/css2?family=Cinzel:wght@400;500&family=Poppins:wght@300;400&display=swap" rel="stylesheet">
<style>
  :root {
    --page-bg: #1c1c1c;
    --card-dark: #2e2e2e;
    --card-back: #252525;
    --pattern-tone: #2c2c2c;
    --card-light: #ffffff;
    --ink-dark: #2a2a2a;
    --ink-light: #ffffff;
    --ink-soft: #d9d9d9;
  }
  * { margin: 0; padding: 0; box-sizing: border-box; }
  html, body {
    width: 1200px; height: 1015px; overflow: hidden;
    background: var(--page-bg);
  }
  .canvas {
    position: relative; width: 1200px; height: 1015px;
    display: flex; flex-direction: column; align-items: center; justify-content: center; gap: 48px;
  }
  .card {
    position: relative; width: 760px; height: 434px; overflow: hidden;
    box-shadow: 0 18px 40px rgba(0,0,0,.55);
  }

  /* Back side */
  .card-back { background: var(--card-back); }
  .brand-pattern {
    position: absolute; inset: 0 0 96px 0;
    background: linear-gradient(160deg, #333 0%, var(--pattern-tone) 50%, #262626 100%);
  }
  .back-highlight {
    position: absolute; left: 470px; top: 170px;
    font-family: "Cinzel", serif; font-weight: 400; font-size: 26px;
    letter-spacing: 3px; color: var(--ink-light);
  }
  .services {
    position: absolute; left: 0; right: 0; bottom: 44px;
    display: flex; justify-content: center; align-items: center; gap: 14px;
    font-family: "Poppins", sans-serif; font-weight: 400; font-size: 17px;
    letter-spacing: 1px; color: var(--ink-light);
  }
  .services .dot { width: 6px; height: 6px; background: var(--ink-light); transform: rotate(45deg); }

  /* Front side */
  .card-front { display: flex; background: var(--card-light); }
  .front-info {
    width: 352px; height: 100%; background: var(--card-dark);
    padding: 118px 0 0 48px; color: var(--ink-light);
  }
  .divider-gap { width: 7px; background: var(--card-light); }
  .divider-line { width: 3px; background: var(--ink-dark); }
  .front-brand {
    flex: 1; display: flex; align-items: center; justify-content: center;
    margin-bottom: 40px;
  }
  .brand-name {
    font-family: "Cinzel", serif; font-weight: 400; font-size: 64px;
    letter-spacing: 6px; color: var(--ink-dark);
  }
  .person-name {
    font-family: "Cinzel", serif; font-weight: 500; font-size: 26px;
    letter-spacing: 1px; line-height: 1;
  }
  .person-title {
    font-family: "Poppins", sans-serif; font-weight: 300; font-size: 17px;
    color: var(--ink-soft); margin-top: 4px;
  }
  .contacts { list-style: none; margin-top: 58px; }
  .contacts li {
    display: flex; align-items: center; gap: 14px; margin-bottom: 10px;
    font-family: "Poppins", sans-serif; font-weight: 300; font-size: 19px;
  }
  .contacts svg { width: 26px; height: 26px; flex: none; }
</style>
</head>
<body>
<main class="canvas">
  <section class="card card-back" aria-label="Business card back">
    <div class="brand-pattern" role="img" aria-label="Faint repeating brand name pattern"></div>
    <span class="back-highlight">TORVEL</span>
    <div class="services">
      <span>AIR</span><span class="dot"></span>
      <span>OCEAN</span><span class="dot"></span>
      <span>FTL</span><span class="dot"></span>
      <span>LTL</span><span class="dot"></span>
      <span>EXPRESS</span>
    </div>
  </section>

  <section class="card card-front" aria-label="Business card front">
    <div class="front-info">
      <h1 class="person-name">ADRIAN HALE</h1>
      <p class="person-title">Managing Director</p>
      <ul class="contacts">
        <li>
          <svg viewBox="0 0 26 26" aria-hidden="true"><rect x="1" y="1" width="24" height="24" fill="none" stroke="#fff" stroke-width="1.4"/><rect x="9" y="6" width="8" height="14" rx="1.5" fill="none" stroke="#fff" stroke-width="1.4"/><line x1="12" y1="17.5" x2="14" y2="17.5" stroke="#fff" stroke-width="1.4"/></svg>
          <span>044-555 010 247</span>
        </li>
        <li>
          <svg viewBox="0 0 26 26" aria-hidden="true"><rect x="1" y="1" width="24" height="24" fill="none" stroke="#fff" stroke-width="1.4"/><path d="M8 7 l3 0 l1.5 3.5 l-2 1.5 a8 8 0 0 0 3.5 3.5 l1.5 -2 l3.5 1.5 l0 3 a2 2 0 0 1 -2 1.5 a12 12 0 0 1 -11 -11 a2 2 0 0 1 1.5 -2z" fill="none" stroke="#fff" stroke-width="1.3"/></svg>
          <span>044-555 010 248</span>
        </li>
        <li>
          <svg viewBox="0 0 26 26" aria-hidden="true"><rect x="1" y="1" width="24" height="24" fill="none" stroke="#fff" stroke-width="1.4"/><rect x="6" y="8" width="14" height="10" fill="#fff"/><path d="M6 8 l7 6 l7 -6" fill="none" stroke="#2e2e2e" stroke-width="1.3"/></svg>
          <span>info@torvelfreight.com</span>
        </li>
      </ul>
    </div>
    <div class="divider-gap"></div>
    <div class="divider-line"></div>
    <div class="front-brand">
      <span class="brand-name">TORVEL</span>
    </div>
  </section>
</main>
</body>
</html>
```